Surgical Sales Presentation Folder

Presentation folder; three panel; custom cutouts; Six 8.5 x 11 full color sales sheets to be bound into presentation folder; 5 full color sales sheets, stepped, longest being 8.5 x 11.
We are Brantley Surgical Group and we are a surgical company that supports physicians who wish to become surgeons. Our clients are Physicians. As such, the design needs to be very professional.
I have included a list of photos and a letter describing what we like about each photo. I have included the verbiage with page identifiers. If this makes scene, please feel free to add photos to the inside of the folder or I can provide you with examples that we think are similar to what we are looking for.
Updates
Target Market(s)
Doctors who want to be surgeons.
Industry/Entity Type
Sales
Requirements
Must have
- Presentation folder; three panel; custom cutouts; Six 8.5 x 11 full color sales sheets to be bound into presentation folder; 5 full color sales sheets, stepped, longest being 8.5 x 11.

```html
<!DOCTYPE html>
<html lang="en">
<head>
<meta charset="utf-8">
<title>Brantley Surgical Group – Presentation Folder</title>
<link href="https://fonts.googleapis.com/css2?family=Arimo:ital,wght@0,400;0,700;1,400&display=swap" rel="stylesheet">
<style>
:root{
  --stage:#1e1e1f;
  --folder:#151516;
  --folder-edge:#2c2c2e;
  --sheet:#ffffff;
  --ink:#1b1b1b;
  --ink-light:#e9e9ea;
  --muted:#9a9a9c;
  --accent:#2ea6dc;
  --accent-deep:#0d5f8c;
  --frame:#3a3a3c;
}
*{box-sizing:border-box;margin:0;padding:0}
html,body{width:1200px;height:460px;overflow:hidden;background:var(--stage)}
body{font-family:"Arimo",Arial,sans-serif;color:var(--ink-light);position:relative}

/* ---------- outside of folder ---------- */
.folder-outside{position:absolute;left:36px;top:40px;width:530px;height:380px;display:flex}
.cover-panel{width:360px;height:100%;background:linear-gradient(180deg,#1b1b1d,#0f0f10);border:1px solid var(--folder-edge);position:relative}
.flap-panel{width:170px;height:100%;background:linear-gradient(180deg,#1d1d1f,#111112);border:1px solid var(--folder-edge);border-left:none;position:relative}
.poster-frame{position:absolute;left:58px;top:28px;width:190px;height:230px;background:var(--frame);padding:8px;box-shadow:0 0 14px rgba(255,255,255,.25)}
.poster-frame .poster{width:100%;height:100%;background:linear-gradient(180deg,#f5efe4,#efc9a0 55%,#e6b88a)}
.brand{display:flex;align-items:center;gap:6px;font-weight:700;color:var(--accent);letter-spacing:.3px}
.brand .dot{border-radius:50%;background:var(--accent);flex:none}
.cover-brand{position:absolute;left:58px;top:282px;font-size:15px}
.cover-brand .dot{width:16px;height:16px}
.contact-list{position:absolute;left:58px;top:310px;list-style:none;font-size:8px;color:var(--ink-light)}
.contact-list li{display:flex;align-items:center;gap:6px;height:13px}
.contact-list svg{width:9px;height:9px;flex:none}
.flap-seal{position:absolute;left:40px;top:110px;width:92px;height:92px;border-radius:50%;background:var(--accent-deep)}
.flap-brand{position:absolute;right:12px;bottom:26px;font-size:10px;color:var(--ink-light);font-weight:400}

/* ---------- inside of folder ---------- */
.folder-inside{position:absolute;left:596px;top:40px;width:572px;height:380px;display:flex;background:var(--folder);border:1px solid var(--folder-edge)}
.inside-panel{width:190px;height:100%;position:relative;border-right:1px solid var(--folder-edge)}
.inside-panel:last-child{border-right:none;width:192px}
.panel-brand{position:absolute;left:14px;top:16px;font-size:12px}
.panel-brand .dot{width:14px;height:14px}
.career{padding:60px 12px 0 14px}
.career h2,.sheet h2,.treatment h2{font-size:11px;font-weight:700;color:var(--accent);margin-bottom:8px}
.career p{font-size:6px;line-height:1.4;margin-bottom:6px}
.career ul{font-size:6px;line-height:1.45;margin:0 0 6px 10px}
.career .quote{position:absolute;left:14px;right:12px;bottom:18px;font-size:6px;font-style:italic;color:var(--accent);line-height:1.4}
.career .quote span{display:block;text-align:right;color:var(--ink-light);margin-top:2px}

.sheets{background:#0e0e0f}
.sheet-step{position:absolute;top:22px;height:340px;background:var(--sheet);border:1px solid #bdbdbd}
.sheet{position:absolute;left:8px;top:22px;width:150px;height:340px;background:var(--sheet);color:var(--ink);padding:16px 10px 0 10px;box-shadow:2px 0 6px rgba(0,0,0,.4)}
.sheet ul{font-size:5.4px;line-height:1.45;margin-left:8px}
.sheet li{margin-bottom:5px}
.sheet .sheet-photo{margin-top:8px;height:80px;background:linear-gradient(135deg,#c9d9e8,#6f8fb0)}
.sheet-footer{position:absolute;left:10px;bottom:8px;font-size:6px;font-weight:700;color:var(--accent-deep)}

.treatment{padding:16px 10px 0 40px}
.treatment .tab{position:absolute;top:0;width:22px;height:100%;background:#1f1f21;border-right:1px solid var(--folder-edge)}
.treatment .tab span{position:absolute;bottom:60px;left:4px;transform:rotate(-90deg);transform-origin:left top;font-size:11px;font-weight:700;color:var(--accent);white-space:nowrap;translate:0 100%}
.treatment p{font-size:5.4px;line-height:1.45;margin-bottom:5px}
.treatment strong{color:var(--accent)}
.pocket{position:absolute;left:24px;right:0;bottom:0;height:74px;background:#111;border-top:1px solid var(--folder-edge);display:flex;align-items:center;justify-content:center}
.pocket .brand{font-size:11px}
.pocket .dot{width:12px;height:12px}
</style>
</head>
<body>

<section class="folder-outside" aria-label="Folder outside">
  <div class="cover-panel">
    <div class="poster-frame"><div class="poster" role="img" aria-label="Framed anatomical poster of the human hair follicle"></div></div>
    <div class="brand cover-brand"><span class="dot"></span>Brantley Surgical Group</div>
    <ul class="contact-list">
      <li><svg viewBox="0 0 10 10"><circle cx="5" cy="5" r="5" fill="#2ea6dc"/><path d="M5 2a2 2 0 0 1 2 2c0 1.5-2 4-2 4S3 5.5 3 4a2 2 0 0 1 2-2z" fill="#111"/></svg>123 somewhere st. here country</li>
      <li><svg viewBox="0 0 10 10"><circle cx="5" cy="5" r="5" fill="#2ea6dc"/><path d="M3 2.5l1.2 0 .5 1.3-.7.6a4 4 0 0 0 1.6 1.6l.6-.7 1.3.5v1.2c-2.8 0-4.5-1.7-4.5-4.5z" fill="#111"/></svg>000-000-0000</li>
      <li><svg viewBox="0 0 10 10"><circle cx="5" cy="5" r="5" fill="#2ea6dc"/><rect x="2.5" y="3.2" width="5" height="3.6" fill="#111"/><path d="M2.5 3.2L5 5.2 7.5 3.2" stroke="#2ea6dc" stroke-width=".6" fill="none"/></svg>email@company.com</li>
      <li><svg viewBox="0 0 10 10"><circle cx="5" cy="5" r="5" fill="#2ea6dc"/><circle cx="5" cy="5" r="2.6" fill="none" stroke="#111" stroke-width=".7"/><path d="M2.4 5h5.2M5 2.4v5.2" stroke="#111" stroke-width=".6"/></svg>www.companyname.com</li>
    </ul>
  </div>
  <div class="flap-panel">
    <div class="flap-seal"></div>
    <div class="flap-brand">Brantley Surgical Group</div>
  </div>
</section>

<section class="folder-inside" aria-label="Folder inside">
  <div class="inside-panel career">
    <div class="brand panel-brand"><span class="dot"></span>Brantley Surgical Group</div>
    <h2>Career Satisfaction</h2>
    <p>What makes a physician happy with their career choice? According to a study conducted at Lakeshore State University, factors that make a significant positive impact on a physician's career satisfaction are:</p>
    <ul>
      <li>The ability to provide quality care</li>
      <li>The ability to spend time with their patients</li>
      <li>Income &amp; Financial Incentives</li>
    </ul>
    <p>In other words, when a physician or a surgeon can make a significant difference in the lives of his patients, providing quality care, while meeting the financial needs of his family, he experiences a far greater degree of career satisfaction.</p>
    <p>Through the years, the high quality of patient care provided by physicians has remained consistent. However, many physicians find themselves needing to spend less time with a greater number of patients.</p>
    <p>What are the results of these trends? A National Business Ledger survey of 12,000 physicians found only 6% described their morale as positive.</p>
    <p class="quote">"In the mid-20th Century, physicians were the pillars of any community. If you were smart, sincere and ambitious, there was nothing nobler or more rewarding that you could aspire to become."<span>-Dr. Samuel Hartwell-</span></p>
  </div>

  <div class="inside-panel sheets">
    <div class="sheet-step" style="left:24px;width:150px;top:30px;height:300px"></div>
    <div class="sheet-step" style="left:20px;width:150px;top:27px;height:315px"></div>
    <div class="sheet-step" style="left:16px;width:150px;top:25px;height:325px"></div>
    <div class="sheet-step" style="left:12px;width:150px;top:23px;height:335px"></div>
    <article class="sheet">
      <h2>The role of BSG</h2>
      <ul>
        <li>We help clients identify and sign up for membership in relevant surgical associations and societies.</li>
        <li>We guide you through the financing options available for starting your surgical practice.</li>
        <li>We provide you with copies of consent forms and protocols that you can customize for your practice.</li>
        <li>We assist you with identification and procurement of relevant literature and training materials.</li>
      </ul>
      <div class="sheet-photo" role="img" aria-label="Photo of a medical caduceus emblem on a blue background"></div>
      <div class="sheet-footer">Brantley Surgical Group</div>
    </article>
  </div>

  <div class="inside-panel treatment">
    <div class="tab" style="left:0"><span>PRP &amp; NovaCell</span></div>
    <h2>PRP &amp; NovaCell</h2>
    <p><strong>What is PRP?</strong><br>PRP or Platelet Rich Plasma is a concentration of autologous platelets in a small volume of plasma with a higher platelet concentration (5-10 times) above the baseline.</p>
    <p><strong>How does PRP work?</strong><br>PRP contains an array of growth factors. These platelet-derived growth factors are directly linked to the biological cascades that induce a faster telogen-to-anagen transition and stimulate the body's own stem cells, which in turn help produce new follicle cells and prolong the anagen phase.</p>
    <p>Studies have also shown a dose-response relationship between platelet concentration and certain proliferative events of significance to wound healing. PRP has been used throughout a large variety of medical specialties.</p>
    <div class="pocket"><div class="brand"><span class="dot"></span>Brantley Surgical Group</div></div>
  </div>
</section>

</body>
</html>
```